Human Resource Consulting Powerpoint / Word Templates

We need Powerpoint and Word templates to use the same style as our new website. We use Powerpoint and Word when presenting to our clients. These must look professional.
- Proposal template for Powerpoint (8 Page layouts see attached)
- Presentation template for Powerpoint (8 Page layouts see attached)
- Letter head ( 1 page)
- Proposal Template for Word
- Report Template for Word
Theses should include a mini style guide including font size, text positioning on the page and image positioning.
Link to website under construction: http://www.brightmeadow.com.au.42.vornatek.pw/
Our new biz card designs and logo file attached.
Consulting
- Helvetica Nue

```html
<!DOCTYPE html>
<html lang="en">
<head>
<meta charset="utf-8">
<title>BrightMeadow HR – Presentation Templates</title>
<link rel="stylesheet" href="https://fonts.googleapis.com/css2?family=Open+Sans:wght@400;600;700&display=swap">
<style>
:root{
  --blue:#1a8fd8;
  --blue-dark:#11609a;
  --ink:#2f3438;
  --grey:#6b7177;
  --light:#eef0f2;
  --canvas:#e6e8eb;
  --slate:#5f7891;
  --photo:linear-gradient(170deg,#7d8792 0%,#4a525c 35%,#2a2f36 70%,#16191d 100%);
}
*{box-sizing:border-box;margin:0;padding:0}
html,body{width:671px;height:1200px;overflow:hidden}
body{background:var(--canvas);font-family:"Open Sans",Arial,sans-serif;color:var(--ink);position:relative}
.slide{position:absolute;width:218px;height:164px;background:#fff;overflow:hidden;box-shadow:0 0 2px rgba(0,0,0,.18)}
.c1{left:3px}.c2{left:227px}.c3{left:451px}
.r1{top:3px}.r2{top:173px}.r3{top:343px}.r4{top:513px}.r5{top:683px}.r6{top:853px}.r7{top:1023px}
.abs{position:absolute}
.photo{position:absolute;background:var(--photo)}
.brand-name{position:absolute;top:8px;right:8px;font-size:5px;font-weight:400;color:var(--grey);white-space:nowrap}
.brand-name.on-dark{color:#fff}
.title{position:absolute;font-size:9px;color:var(--blue);font-weight:400;white-space:nowrap}
.body{position:absolute;font-size:4px;line-height:1.35;color:var(--grey)}
.body p{margin-bottom:4px}
.center{text-align:center}
.pg{position:absolute;right:4px;bottom:4px;width:7px;height:7px;border-radius:50%;background:var(--blue);color:#fff;font-size:3.6px;display:flex;align-items:center;justify-content:center}
.vdots{position:absolute;left:3px;top:3px;width:4px;height:34px;background:radial-gradient(circle,var(--blue) 1.2px,transparent 1.5px) 0 0/4px 4px}
.hdots{position:absolute;bottom:5px;width:44px;height:4px;background:radial-gradient(circle,var(--blue) 1.2px,transparent 1.5px) 0 0/4px 4px;opacity:.85}
.num{width:8px;height:8px;border-radius:50%;border:1px solid var(--blue);background:var(--blue);color:#fff;font-size:3.8px;display:inline-flex;align-items:center;justify-content:center;box-shadow:0 0 0 1px #fff,0 0 0 1.6px var(--blue);flex:none}
.list{position:absolute;display:flex;flex-direction:column;gap:10px}
.item{display:flex;align-items:center;gap:6px;font-size:4.4px;color:var(--grey)}
.badge{position:absolute;width:20px;height:20px;border-radius:50%;background:var(--blue);color:#fff;font-size:3.6px;line-height:1.1;display:flex;align-items:center;justify-content:center;text-align:center;box-shadow:0 0 0 1.5px #fff,0 0 0 2.3px var(--blue)}
.topbar{position:absolute;left:0;top:0;width:100%;height:26px;background:#fff}
.client-name{position:absolute;left:6px;top:9px;font-size:6px;font-weight:400;color:var(--blue)}
.cover-box{position:absolute;left:108px;top:59px;width:95px;height:42px;background:rgba(26,143,216,.55);padding:6px 10px;color:#fff}
.cover-box h1{font-size:13px;font-weight:400;line-height:1}
.cover-box .sub{font-size:5px;margin-top:2px}
.cover-box .date{font-size:3.6px}
.footbar{position:absolute;left:0;bottom:0;width:100%;height:18px;background:rgba(15,18,22,.75);color:#fff;display:flex;align-items:center;padding:0 5px;gap:4px;font-size:3.6px}
.person{display:flex;align-items:center;gap:3px}
.person::before{content:"";width:6px;height:6px;border-radius:50%;background:var(--blue)}
.person b{display:block;font-size:5px;font-weight:400}
.person span{display:block;color:var(--blue);font-size:3.4px}
.panel{position:absolute;background:#fff}
.client{display:flex;align-items:center;justify-content:center;text-align:center;font-size:4px;font-weight:400;color:var(--ink);border-right:.5px solid #ddd;border-bottom:.5px solid #ddd}
table{border-collapse:collapse;width:100%;font-size:3.2px;color:var(--grey)}
td{height:6.4px;border-bottom:.4px solid #ccc;text-align:center}
td:first-child{text-align:left;padding-left:3px}
.dot{display:inline-block;width:2px;height:2px;border-radius:50%;background:var(--ink)}
.row-info{display:flex;gap:4px;font-size:3.8px;color:var(--grey);align-items:center;height:7px;white-space:nowrap}
.row-info i{width:5px;height:5px;border-radius:50%;background:var(--blue);flex:none}
.row-info em{font-style:normal;width:22px;color:var(--ink)}
</style>
</head>
<body>

<!-- 1 Proposal cover -->
<section class="slide c1 r1">
  <div class="photo" style="inset:0" role="img" aria-label="Snow-covered mountain range under a dark sky"></div>
  <div class="topbar"></div>
  <div class="client-name">Harbour Bank</div>
  <div class="brand-name">BrightMeadow HR</div>
  <div class="cover-box"><h1>Proposal</h1><div class="sub">Corporation</div><div class="date">July, 1st 2016</div></div>
  <div class="footbar">For <div class="person"><div><b>Mr. Dan Porter</b><span>Vice President</span></div></div>
    <span style="margin-left:auto">From</span><div class="person"><div><b>Lena Whitford</b><span>Director of Consulting</span></div></div></div>
</section>

<!-- 2 Presentation cover -->
<section class="slide c2 r1">
  <div class="photo" style="inset:0" role="img" aria-label="Snow-covered mountain range under a dark sky"></div>
  <div class="topbar"></div>
  <div class="client-name">Harbour Bank</div>
  <div class="brand-name">BrightMeadow HR</div>
  <div class="cover-box"><h1>Presentation</h1><div class="sub">Subtitle here</div><div class="date">August, 1st 2016</div></div>
  <div class="footbar"><div class="person"><div><b>Lena Whitford</b><span>Director of Consulting</span></div></div></div>
</section>

<!-- 3 Content -->
<section class="slide c3 r1">
  <div class="vdots"></div>
  <div class="title" style="left:13px;top:10px">Content</div>
  <div class="brand-name">BrightMeadow HR</div>
  <div class="list" style="left:36px;top:48px">
    <div class="item"><span class="num">1</span>Content No. 1</div>
    <div class="item"><span class="num">2</span>Content No. 2</div>
    <div class="item"><span class="num">3</span>Content No. 3</div>
    <div class="item"><span class="num">4</span>Content No. 4</div>
    <div class="item"><span class="num">5</span>Content No. 5</div>
  </div>
  <div class="list" style="left:122px;top:48px">
    <div class="item"><span class="num">6</span>Content No. 6</div>
    <div class="item"><span class="num">7</span>Content No. 7</div>
    <div class="item"><span class="num">8</span>Content No. 8</div>
    <div class="item"><span class="num">9</span>Content No. 9</div>
    <div class="item"><span class="num">10</span>Content No. 10</div>
  </div>
  <div class="pg">3</div>
</section>

<!-- 4 Large Image Right -->
<section class="slide c1 r2">
  <div class="vdots"></div>
  <div class="title" style="left:13px;top:10px">Large Image Right</div>
  <div class="photo" style="left:108px;top:0;width:110px;height:164px" role="img" aria-label="Snowy mountain peak"></div>
  <div class="brand-name on-dark">BrightMeadow HR</div>
  <div class="badge" style="left:98px;top:70px">Your<br>Text</div>
  <div class="body" style="left:13px;top:46px;width:80px">
    <p>BrightMeadow HR is a human resource consultancy transforming businesses all over Australia. We combine HR and Strategy to create the momentum behind great businesses.</p>
    <p>We believe that people are at the heart of every great business. To achieve real growth, businesses need to continuously refine the way they measure, manage and motivate their people.</p>
    <p>We refer to this as the Journey to Greatness and pride ourselves in taking businesses on this journey so they can achieve great things.</p>
  </div>
  <div class="pg">4</div>
</section>

<!-- 5 Image Left -->
<section class="slide c2 r2">
  <div class="vdots"></div>
  <div class="brand-name">BrightMeadow HR</div>
  <div class="abs" style="left:12px;top:62px;width:60px;height:60px;border-radius:50%;background:radial-gradient(circle at 40% 35%,#7a746d,#4a4540 60%,#2c2926)" role="img" aria-label="Round weathered stone with a hole in the centre"></div>
  <div class="title" style="left:94px;top:40px">Image Left</div>
  <div class="body" style="left:94px;top:62px;width:105px">
    <p>BrightMeadow HR is a human resource consultancy transforming businesses all over Australia. We combine HR and Strategy to create the momentum behind great businesses.</p>
    <p>We believe that people are at the heart of every great business. To achieve real growth, businesses need to continuously refine the way they measure, manage and motivate their people.</p>
    <p>We refer to this as the Journey to Greatness and pride ourselves in taking businesses on this journey so they can achieve great things.</p>
  </div>
  <div class="pg">5</div>
</section>

<!-- 6 Image top -->
<section class="slide c3 r2">
  <div class="photo" style="left:0;top:0;width:218px;height:110px" role="img" aria-label="Wide view of a snow-covered mountain ridge"></div>
  <div class="brand-name on-dark" style="left:8px;right:auto">BrightMeadow HR</div>
  <div class="badge" style="left:14px;top:100px">Your<br>Text</div>
  <div class="body" style="left:12px;top:121px;width:198px">
    <p style="margin-bottom:2px;padding-left:30px">BrightMeadow HR is a human resource consultancy transforming businesses all over Australia. We combine HR and Strategy to create the momentum behind great businesses.</p>
    <p>We believe that people are at the heart of every great business. To achieve real growth, businesses need to continuously refine the way they measure, manage and motivate their people.</p>
  </div>
  <div class="hdots" style="left:162px;bottom:4px;width:40px"></div>
  <div class="pg">6</div>
</section>

<!-- 7 Heading & Text -->
<section class="slide c1 r3">
  <div class="brand-name" style="left:8px;right:auto">BrightMeadow HR</div>
  <div class="title" style="left:0;width:100%;top:32px;text-align:center">Heading &amp; Text</div>
  <div class="body center" style="left:18px;top:58px;width:182px">
    <p>BrightMeadow HR is a human resource consultancy transforming businesses all over Australia. We combine HR and Strategy to create the momentum behind great businesses.</p>
    <p>We believe that people are at the heart of every great business. To achieve real growth, businesses need to continuously refine the way they measure, manage and motivate their people.</p>
    <p>We refer to this as the Journey to Greatness and pride ourselves in taking businesses on this journey so they can achieve great things.</p>
  </div>
  <div class="hdots" style="left:160px"></div>
  <div class="pg">7</div>
</section>

<!-- 8 Quote -->
<section class="slide c2 r3" style="background:var(--light)">
  <div class="brand-name" style="left:8px;right:auto">BrightMeadow HR</div>
  <div class="badge" style="left:99px;top:46px;font-size:11px;font-weight:700">&ldquo;</div>
  <div class="abs" style="left:26px;top:72px;font-size:16px;color:var(--grey)">&ldquo;</div>
  <div class="abs center" style="left:34px;top:78px;width:150px;font-size:5px;line-height:1.45;color:var(--ink)">It is not the strongest of the species that survives,<br>nor the most intelligent that survives.<br>It is the one that is most adaptable to change.</div>
  <div class="abs center" style="left:0;width:100%;top:106px;font-size:3.6px;color:var(--blue)">- R. Halvorsen -</div>
  <div class="abs" style="left:180px;top:98px;font-size:16px;color:var(--grey)">&rdquo;</div>
  <div class="hdots" style="left:160px"></div>
  <div class="pg">8</div>
</section>

<!-- 9 Bullet Area -->
<section class="slide c3 r3">
  <div class="vdots"></div>
  <div class="title" style="left:13px;top:10px">Bullet Area</div>
  <div class="brand-name">BrightMeadow HR</div>
  <div class="abs" style="left:0;top:110px;width:62px;height:54px;background:linear-gradient(160deg,#f3f3f3 0%,#cfcfcf 40%,#1e1e1e 60%,#0c0c0c 100%)" role="img" aria-label="Hand in a dark suit sleeve held out palm up"></div>
  <div class="list" style="left:86px;top:34px">
    <div class="item"><span class="num">1</span>Bullets and Numbering 1</div>
    <div class="item"><span class="num">2</span>Bullets and Numbering 2</div>
    <div class="item"><span class="num">3</span>Bullets and Numbering 3</div>
    <div class="item"><span class="num">4</span>Bullets and Numbering 4</div>
    <div class="item"><span class="num">5</span>Bullets and Numbering 5</div>
    <div class="item"><span class="num">6</span>Bullets and Numbering 6</div>
  </div>
  <div class="pg">9</div>
</section>

<!-- 10 Special Offer -->
<section class="slide c1 r4">
  <div class="photo" style="inset:0" role="img" aria-label="Snow-covered mountains"></div>
  <div class="brand-name on-dark" style="left:8px;right:auto">BrightMeadow HR</div>
  <div class="panel" style="left:10px;top:38px;width:200px;height:90px">
    <div class="title" style="left:8px;top:7px;font-size:6px">Special Offer</div>
    <ul class="body" style="left:14px;top:20px;width:92px;padding-left:3px">
      <li style="margin-bottom:6px">BrightMeadow HR is a human resource consultancy transforming businesses all over Australia. We combine HR and Strategy to create the momentum behind great businesses.</li>
      <li>We believe that people are at the heart of every great business. To achieve real growth, businesses need to continuously refine the way they measure, manage and motivate their people.</li>
    </ul>
    <div class="abs" style="left:116px;top:16px;width:74px;height:44px;border-radius:5px;border:2px solid var(--slate);background:linear-gradient(140deg,#c9d2da,#6d7c89 60%,#3e4a55)" role="img" aria-label="Team members joining hands in a circle"></div>
    <div class="hdots" style="left:136px;bottom:5px;width:40px"></div>
  </div>
  <div class="pg">10</div>
</section>

<!-- 11 Three text columns with image -->
<section class="slide c2 r4">
  <div class="title" style="left:8px;top:10px">BrightMeadow</div>
  <div class="brand-name">BrightMeadow HR</div>
  <div class="body" style="left:8px;top:44px;width:62px">
    <p>BrightMeadow HR is a human resource consultancy transforming businesses all over Australia. We combine HR and Strategy to create the momentum behind great businesses.</p>
    <p>We believe that people are at the heart of every great business. To achieve real growth, businesses need to continuously refine the way they measure, manage and motivate their people.</p>
    <p>We refer to this as the Journey to Greatness and pride ourselves in taking businesses on this journey so they can achieve great things.</p>
  </div>
  <div class="abs" style="left:74px;top:44px;width:70px;height:110px;background:linear-gradient(180deg,#2f5778,#4d7da3 55%,#1c3348)" role="img" aria-label="Lighthouse on a rocky headland at dusk"></div>
  <div class="body" style="left:150px;top:44px;width:62px">
    <p>BrightMeadow HR is a human resource consultancy transforming businesses all over Australia. We combine HR and Strategy to create the momentum behind great businesses.</p>
    <p>We believe that people are at the heart of every great business. To achieve real growth, businesses need to continuously refine the way they measure, manage and motivate their people.</p>
    <p>We refer to this as the Journey to Greatness and pride ourselves in taking businesses on this journey so they can achieve great things.</p>
  </div>
  <div class="pg">11</div>
</section>

<!-- 12 Our Clients -->
<section class="slide c3 r4">
  <div class="photo" style="inset:0" role="img" aria-label="Snow-covered mountains"></div>
  <div class="brand-name on-dark" style="left:8px;right:auto">BrightMeadow HR</div>
  <div class="panel" style="left:9px;top:38px;width:200px;height:90px">
    <div class="abs center" style="left:0;width:100%;top:4px;font-size:8px;color:var(--blue)">Our Clients</div>
    <div class="abs center" style="left:0;width:100%;top:15px;font-size:4px;color:var(--grey)">We work across all industries</div>
    <div class="abs" style="left:4px;top:24px;width:192px;height:50px;display:grid;grid-template-columns:repeat(5,1fr);grid-template-rows:1fr 1fr">
      <div class="client">Harbour Bank</div><div class="client">Norvik</div><div class="client">Quarrow</div><div class="client">Fenmore</div><div class="client">Tidewell Council</div>
      <div class="client">Ashcombe</div><div class="client">Pellard</div><div class="client">Larkfield Group</div><div class="client">Corvale</div><div class="client">Greystone Labs</div>
    </div>
    <div class="hdots" style="left:146px;bottom:3px;width:40px"></div>
  </div>
  <div class="pg">12</div>
</section>

<!-- 13 Chart Area -->
<section class="slide c1 r5">
  <div class="vdots"></div>
  <div class="title" style="left:13px;top:10px">Chart Area</div>
  <div class="brand-name">BrightMeadow HR</div>
  <ul class="body" style="left:30px;top:28px;width:160px">
    <li>BrightMeadow HR is a human resource consultancy transforming businesses all over Australia. We combine HR and Strategy to create the momentum behind great businesses.</li>
  </ul>
  <div class="abs" style="left:36px;top:78px;display:flex;flex-direction:column;gap:10px;font-size:3.6px;color:var(--grey)">
    <div style="display:flex;align-items:center;gap:4px"><i style="width:8px;height:8px;border-radius:50%;background:var(--blue)"></i><span style="width:26px">Category 1</span><b style="font-size:8px;font-weight:400;color:var(--blue)">60%</b></div>
    <div style="display:flex;align-items:center;gap:4px"><i style="width:8px;height:8px;border-radius:50%;background:var(--slate)"></i><span style="width:26px">Category 2</span><b style="font-size:8px;font-weight:400;color:var(--blue)">30%</b></div>
    <div style="display:flex;align-items:center;gap:4px"><i style="width:8px;height:8px;border-radius:50%;background:var(--ink)"></i><span style="width:26px">Category 3</span><b style="font-size:8px;font-weight:400;color:var(--blue)">10%</b></div>
  </div>
  <svg class="abs" style="left:118px;top:74px" width="60" height="60" viewBox="0 0 60 60">
    <g transform="rotate(-90 30 30)" fill="none" stroke-width="8">
      <circle cx="30" cy="30" r="24" stroke="#1a8fd8" stroke-dasharray="90.5 150.8"/>
      <circle cx="30" cy="30" r="24" stroke="#5f7891" stroke-dasharray="45.2 150.8" stroke-dashoffset="-90.5"/>
      <circle cx="30" cy="30" r="24" stroke="#2f3438" stroke-dasharray="15.1 150.8" stroke-dashoffset="-135.7"/>
    </g>
    <text x="30" y="33" text-anchor="middle" font-size="8" fill="#2f3438" font-family="Open Sans, sans-serif">Chart</text>
  </svg>
  <div class="pg">13</div>
</section>

<!-- 14 How we help -->
<section class="slide c2 r5">
  <div class="vdots"></div>
  <div class="title" style="left:13px;top:10px">How we help our clients</div>
  <div class="brand-name">BrightMeadow HR</div>
  <div class="abs" style="left:7px;top:50px;width:206px;display:grid;grid-template-columns:repeat(5,1fr);gap:6px">
    <div><div style="height:36px;border:1.5px solid #c9ccd0;background:linear-gradient(160deg,#b9c0c7,#5d6670)" role="img" aria-label="Snowy landscape"></div><div style="font-size:3.4px;color:var(--blue);margin:4px 0 3px">The Foundations of Greatness</div><div style="font-size:3.2px;line-height:1.35;color:var(--grey)">We provide advice, policies &amp; templates to keep you compliant</div></div>
    <div><div style="height:36px;border:1.5px solid #c9ccd0;background:linear-gradient(180deg,#3a4b5c,#7890a6)" role="img" aria-label="Lighthouse at night"></div><div style="font-size:3.4px;color:var(--blue);margin:4px 0 3px">The Heart of Greatness</div><div style="font-size:3.2px;line-height:1.35;color:var(--grey)">We set you up with the critical people systems that sit at the core of great business</div></div>
    <div><div style="height:36px;border:1.5px solid #c9ccd0;background:linear-gradient(160deg,#6a727b,#1e2226)" role="img" aria-label="Dark rocky peak"></div><div style="font-size:3.4px;color:var(--blue);margin:4px 0 3px">Resourcing Greatness</div><div style="font-size:3.2px;line-height:1.35;color:var(--grey)">We ensure you can attract and hire the right people to maintain your momentum</div></div>
    <div><div style="height:36px;border:1.5px solid #c9ccd0;background:linear-gradient(160deg,#dfe4e9,#7f8b97)" role="img" aria-label="Climber on a snowy summit"></div><div style="font-size:3.4px;color:var(--blue);margin:4px 0 3px">Developing Greatness</div><div style="font-size:3.2px;line-height:1.35;color:var(--grey)">We ensure you have star players and star teams at all levels</div></div>
    <div><div style="height:36px;border:1.5px solid #c9ccd0;background:linear-gradient(180deg,#8fa2b4,#eef1f4)" role="img" aria-label="Snow field under open sky"></div><div style="font-size:3.4px;color:var(--blue);margin:4px 0 3px">Embedding Greatness</div><div style="font-size:3.2px;line-height:1.35;color:var(--grey)">We embed HR specialists in your business to power your momentum</div></div>
  </div>
  <div class="hdots" style="left:160px"></div>
  <div class="pg">14</div>
</section>

<!-- 15 3 Column Area -->
<section class="slide c3 r5">
  <div class="vdots"></div>
  <div class="brand-name">BrightMeadow HR</div>
  <div class="title" style="left:0;width:100%;top:24px;text-align:center">3 Column Area</div>
  <div class="abs" style="left:6px;top:46px;width:206px;height:100px;display:grid;grid-template-columns:repeat(3,1fr)">
    <div class="center" style="padding:0 6px">
      <svg width="22" height="22" viewBox="0 0 22 22"><circle cx="11" cy="11" r="10" fill="#1a8fd8"/><path d="M12.5 4 7 12h4l-1.5 6L15 10h-4z" fill="#fff"/></svg>
      <div style="font-size:4px;color:var(--blue);margin:4px 0">Column 1</div>
      <div style="font-size:3.6px;line-height:1.35;color:var(--grey)">BrightMeadow HR is a human resource consultancy transforming businesses all over Australia. We combine HR and Strategy to create the momentum behind great businesses.</div>
    </div>
    <div class="center" style="padding:0 6px;border-left:.5px solid #ddd;border-right:.5px solid #ddd">
      <svg width="22" height="22" viewBox="0 0 22 22"><circle cx="11" cy="11" r="10" fill="#1a8fd8"/><circle cx="11" cy="11" r="3" fill="#fff"/><g stroke="#fff" stroke-width="1"><path d="M11 4.5v2M11 15.5v2M4.5 11h2M15.5 11h2M6.4 6.4l1.4 1.4M14.2 14.2l1.4 1.4M6.4 15.6l1.4-1.4M14.2 7.8l1.4-1.4"/></g></svg>
      <div style="font-size:4px;color:var(--blue);margin:4px 0">Column 2</div>
      <div style="font-size:3.6px;line-height:1.35;color:var(--grey)">BrightMeadow HR is a human resource consultancy transforming businesses all over Australia. We combine HR and Strategy to create the momentum behind great businesses.</div>
    </div>
    <div class="center" style="padding:0 6px">
      <svg width="22" height="22" viewBox="0 0 22 22"><circle cx="11" cy="11" r="10" fill="#1a8fd8"/><path d="M7 5h8l-3 6 3 6H7l3-6z" fill="#fff"/></svg>
      <div style="font-size:4px;color:var(--blue);margin:4px 0">Column 3</div>
      <div style="font-size:3.6px;line-height:1.35;color:var(--grey)">BrightMeadow HR is a human resource consultancy transforming businesses all over Australia. We combine HR and Strategy to create the momentum behind great businesses.</div>
    </div>
  </div>
  <div class="pg">15</div>
</section>

<!-- 16 Professional Fees -->
<section class="slide c1 r6">
  <div class="title" style="left:13px;top:10px">Professional Fees</div>
  <div class="brand-name">BrightMeadow HR</div>
  <div class="abs" style="left:8px;top:38px;width:202px;height:104px;box-shadow:0 1px 3px rgba(0,0,0,.25);background:#fff">
    <div class="abs" style="left:0;top:0;width:80px;height:26px;background:var(--blue);color:#fff;font-size:4px;font-weight:600;padding:11px 4px">Description</div>
    <div class="abs center" style="left:80px;top:0;width:61px;height:26px;background:var(--slate);color:#fff;font-size:4px;padding-top:2px">Column 1
      <svg style="display:block;margin:2px auto 0" width="13" height="13" viewBox="0 0 13 13"><circle cx="6.5" cy="6.5" r="6" fill="#fff"/><path d="M7.3 2.5 4 7h2.4l-.8 3.5L9 6H6.6z" fill="#5f7891"/></svg></div>
    <div class="abs center" style="left:141px;top:0;width:61px;height:26px;background:var(--ink);color:#fff;font-size:4px;padding-top:2px">Column 2
      <svg style="display:block;margin:2px auto 0" width="13" height="13" viewBox="0 0 13 13"><circle cx="6.5" cy="6.5" r="6" fill="#fff"/><circle cx="6.5" cy="6.5" r="2" fill="#2f3438"/></svg></div>
    <table class="abs" style="left:0;top:34px;width:202px">
      <colgroup><col style="width:80px"><col style="width:61px"><col style="width:61px"></colgroup>
      <tr><td>Description 1</td><td><span class="dot"></span></td><td><span class="dot"></span></td></tr>
      <tr><td>Description 2</td><td><span class="dot"></span></td><td><span class="dot"></span></td></tr>
      <tr><td>Description 3</td><td><span class="dot"></span></td><td><span class="dot"></span></td></tr>
      <tr><td>Description 4</td><td><span class="dot"></span></td><td><span class="dot"></span></td></tr>
      <tr><td>Description 5</td><td>Text Column 1</td><td>Text Column 2</td></tr>
      <tr><td>Description 6</td><td>-</td><td>-</td></tr>
      <tr><td>Description 7</td><td>Text Column 1</td><td>Text Column 2</td></tr>
      <tr><td>Description 8</td><td><span class="dot"></span></td><td><span class="dot"></span></td></tr>
    </table>
  </div>
  <div class="hdots" style="left:160px"></div>
  <div class="pg">16</div>
</section>

<!-- 17 Steps Area -->
<section class="slide c2 r6">
  <div class="vdots"></div>
  <div class="title" style="left:13px;top:10px">Steps Area</div>
  <div class="brand-name">BrightMeadow HR</div>
  <svg class="abs" style="left:0;top:0" width="218" height="164" viewBox="0 0 218 164">
    <g fill="none" stroke="#1a8fd8" stroke-width=".8">
      <path d="M52 80H176"/>
      <path d="M107 80V67M107 39V47"/>
      <path d="M52 80Q52 96 59 98M176 80Q176 96 168 98"/>
    </g>
    <g fill="#1a8fd8"><circle cx="52" cy="80" r="2"/><circle cx="107" cy="80" r="2"/><circle cx="176" cy="80" r="2"/><circle cx="79" cy="80" r="1.4"/><circle cx="142" cy="80" r="1.4"/><path d="M104.5 40 107 36l2.5 4z"/></g>
    <g font-family="Open Sans, sans-serif" font-size="5" fill="#fff" text-anchor="middle">
      <circle cx="107" cy="57" r="7" fill="#1a8fd8" stroke="#fff" stroke-width="1.2"/><circle cx="107" cy="57" r="8.2" fill="none" stroke="#1a8fd8" stroke-width=".6"/><text x="107" y="59">2</text>
      <circle cx="69" cy="98" r="7" fill="#1a8fd8" stroke="#fff" stroke-width="1.2"/><circle cx="69" cy="98" r="8.2" fill="none" stroke="#1a8fd8" stroke-width=".6"/><text x="69" y="100">1</text>
      <circle cx="158" cy="98" r="7" fill="#1a8fd8" stroke="#fff" stroke-width="1.2"/><circle cx="158" cy="98" r="8.2" fill="none" stroke="#1a8fd8" stroke-width=".6"/><text x="158" y="100">3</text>
    </g>
  </svg>
  <div class="abs center" style="left:70px;top:10px;width:74px;font-size:4px;color:var(--blue);font-weight:600">Step 2</div>
  <div class="body center" style="left:66px;top:16px;width:82px">BrightMeadow HR is a human resource consultancy transforming businesses all over Australia.</div>
  <div class="abs" style="left:24px;top:110px;font-size:4px;color:var(--blue);font-weight:600">Step 1</div>
  <div class="body center" style="left:20px;top:116px;width:84px">BrightMeadow HR is a human resource consultancy transforming businesses all over Australia. We combine HR and Strategy to create the momentum behind great businesses.</div>
  <div class="abs" style="left:176px;top:110px;font-size:4px;color:var(--blue);font-weight:600">Step 3</div>
  <div class="body center" style="left:116px;top:116px;width:84px">BrightMeadow HR is a human resource consultancy transforming businesses all over Australia. We combine HR and Strategy to create the momentum behind great businesses.</div>
  <div class="pg">17</div>
</section>

<!-- 18 Contact -->
<section class="slide c3 r6">
  <div class="vdots"></div>
  <div class="title" style="left:13px;top:10px">Contact</div>
  <div class="brand-name">BrightMeadow HR</div>
  <div class="abs" style="left:14px;top:52px;width:56px;height:60px;border-radius:4px;border:2px solid #c9ccd0;background:linear-gradient(180deg,#d9dcdf,#a7adb3)" role="img" aria-label="Portrait photo of the consultant"></div>
  <div class="abs" style="left:78px;top:54px;font-size:8.5px;color:var(--blue)">Lena Whitford</div>
  <div class="abs" style="left:78px;top:66px;font-size:4px;color:var(--ink)">Director of Consulting</div>
  <div class="abs" style="left:78px;top:74px">
    <div class="row-info"><i></i><em>Email</em>: info@brightmeadowhr.com.au</div>
    <div class="row-info"><i></i><em>Website</em>: www.brightmeadow.com.au.42.vornatek.pw</div>
    <div class="row-info"><i></i><em>Phone</em>: 1300 55 0142</div>
    <div class="row-info"><i></i><em>LinkedIn</em>: linkedin.com/lenawhitford</div>
  </div>
  <div class="hdots" style="left:160px"></div>
  <div class="pg">18</div>
</section>

<!-- 19 Thank You -->
<section class="slide c1 r7">
  <div class="photo" style="inset:0" role="img" aria-label="Snow-covered mountain range"></div>
  <div class="abs" style="left:22px;top:56px;font-size:13px;color:#fff">Thank You</div>
  <div class="abs" style="left:30px;top:74px;font-size:5px;color:var(--blue)">For your attention</div>
  <div class="abs" style="left:0;bottom:0;width:100%;height:34px;background:rgba(15,18,22,.8);color:#fff;font-size:3.6px;padding:5px 6px;display:flex;gap:20px">
    <div style="display:flex;flex-direction:column;gap:2px">
      <div class="row-info" style="color:#fff;height:6px"><i></i>1300 55 0142</div>
      <div class="row-info" style="color:#fff;height:6px"><i></i>info@brightmeadowhr.com.au</div>
      <div class="row-info" style="color:#fff;height:6px"><i></i>www.brightmeadow.com.au.42.vornatek.pw</div>
    </div>
    <div class="row-info" style="color:#fff;align-items:flex-start;height:auto;white-space:normal"><i></i><span style="line-height:1.35">Bright Meadow Pty Ltd<br>Head Office<br>Level 12, Kestrel House - 40 Alder Street<br>Sydney NSW 2000</span></div>
  </div>
</section>

</body>
</html>
```